Design a Website Mockup for а Headache Center - Improve Current Design

I need polishing and improvement of the design of http://www.zornikamed.bg. This a site for a Headache Center (medical clinic). I do not want drastic layout changes, just want the current design made more attractive, using colors, accents, margins, sizes, positioning, etc. For example, right now the design is quite monochromatic - pretty much one green color. I would like to have perhaps the buttons or something else be a different color for accent. Basically, I want to make the design more attractive, but not completely replace it.

Please submit a mockup in Photoshop or Illustrator of the following pages showing also mouse-hover effects:
- Home page - http://zornikamed.bg
- Headaches - http://zornikamed.bg/headaches
- Contact Us - http://zornikamed.bg/contactus

If you open the site in Google Chrome, it will offer you to translate it. That way you can get a better idea of the content.

If the link above does not work please use http://www.vetrilomedic.bg.

```html
<!DOCTYPE html>
<html lang="en">
<head>
<meta charset="utf-8">
<title>Zornika Med — Headache Center</title>
<link href="https://fonts.googleapis.com/css2?family=Bebas+Neue&family=Arimo:ital,wght@0,400;0,700;1,400&display=swap" rel="stylesheet">
<style>
  :root {
    --green: #5cab26;
    --green-dark: #3f8a14;
    --green-light: #7cc542;
    --blue: #0b57a4;
    --ink: #222;
    --line: #d9d9d9;
    --tab: #ececec;
    --panel: #fff;
  }
  * { box-sizing: border-box; margin: 0; padding: 0; }
  html, body { width: 1200px; height: 808px; overflow: hidden; background: #fff; }
  body { position: relative; font-family: "Arimo", Arial, sans-serif; color: var(--ink); }

  .brand { position: absolute; left: 200px; top: 10px; display: flex; align-items: center; gap: 12px; }
  .brand-mark { width: 50px; height: 50px; border-radius: 50%; background: var(--green); }
  .brand-name { font-family: "Arimo", Arial, sans-serif; font-weight: 700; font-size: 28px; line-height: 1; color: var(--green); text-transform: uppercase; letter-spacing: 1px; }

  .call-box { position: absolute; left: 865px; top: 7px; width: 135px; height: 53px; background: var(--green); color: #fff; padding: 6px 10px; }
  .call-label { font-family: "Bebas Neue", sans-serif; font-size: 22px; line-height: 1; letter-spacing: 1px; }
  .call-number { font-family: "Bebas Neue", sans-serif; font-size: 17px; letter-spacing: 1px; }
  .call-box svg { position: absolute; right: 6px; bottom: 5px; }

  .main-nav { position: absolute; left: 200px; top: 78px; display: flex; gap: 6px; }
  .main-nav a { display: block; height: 29px; line-height: 29px; padding: 0 14px; background: var(--tab); color: #333; font-size: 12.5px; text-decoration: none; }
  .main-nav a.is-active { background: var(--green); color: #fff; }
  .nav-rule { position: absolute; left: 191px; top: 107px; width: 820px; height: 5px; background: var(--green); }

  .panel { position: absolute; background: var(--panel); border: 1px solid var(--line); box-shadow: 0 6px 10px -6px rgba(0,0,0,.18); }
  .hero { left: 191px; top: 112px; width: 820px; height: 308px; border-top: none; }
  .hero-title { position: absolute; left: 15px; top: 42px; font-family: "Bebas Neue", sans-serif; font-size: 40px; color: var(--blue); letter-spacing: 2px; line-height: 1; }
  .hero-text { position: absolute; left: 15px; top: 88px; font-size: 10.5px; line-height: 19px; color: #222; white-space: nowrap; }
  .hero-text p + p { margin-top: 19px; }
  .hero-cta { position: absolute; left: 15px; top: 232px; width: 360px; height: 30px; background: var(--blue); color: #fff; font-size: 16px; line-height: 30px; padding-left: 60px; text-decoration: none; box-shadow: 0 3px 4px rgba(0,0,0,.25); }
  .hero-cta svg { position: absolute; left: -2px; top: 2px; }
  .hero-figure { position: absolute; left: 456px; top: 20px; width: 326px; height: 242px; background: linear-gradient(180deg, #f7f7f7, #ececec); }
  .slider-arrow { position: absolute; top: 146px; width: 24px; height: 24px; border-radius: 50%; background: #444; color: #fff; font-size: 16px; line-height: 22px; text-align: center; }
  .slider-prev { left: 464px; }
  .slider-next { left: 753px; }
  .slider-dots { position: absolute; left: 602px; top: 262px; display: flex; gap: 4px; }
  .slider-dots span { width: 9px; height: 9px; border-radius: 50%; border: 1px solid #bbb; }
  .slider-dots span.is-active { background: var(--blue); border-color: var(--blue); }

  .panel-head { height: 40px; background: linear-gradient(180deg, var(--green-light), var(--green)); color: #fff; font-family: "Bebas Neue", sans-serif; font-size: 24px; line-height: 42px; padding-left: 16px; letter-spacing: 1px; }
  .blog { left: 191px; top: 451px; width: 517px; height: 189px; }
  .post-thumb { position: absolute; left: 20px; top: 64px; width: 105px; height: 104px; background: #e3e3e3; }
  .post-body { position: absolute; left: 142px; top: 62px; font-size: 12px; }
  .post-title { color: var(--blue); font-weight: 400; font-size: 12.5px; }
  .post-date { margin-top: 13px; }
  .post-excerpt { margin-top: 13px; }
  .post-more { display: block; margin-top: 13px; font-style: italic; color: #333; text-decoration: none; }

  .newsletter { left: 724px; top: 451px; width: 287px; height: 189px; }
  .newsletter-label { position: absolute; left: 22px; top: 62px; font-size: 12px; color: var(--blue); }
  .newsletter-input { position: absolute; left: 22px; top: 90px; width: 240px; height: 35px; border: 1px solid #bbb; box-shadow: inset 0 1px 3px rgba(0,0,0,.15); font: 11px "Arimo", sans-serif; padding-left: 14px; color: #333; }
  .btn-blue { position: absolute; background: var(--blue); color: #fff; font-family: "Bebas Neue", sans-serif; letter-spacing: 1px; text-align: center; text-decoration: none; }
  .newsletter .btn-blue { left: 22px; top: 141px; width: 117px; height: 31px; font-size: 19px; line-height: 33px; }

  .site-footer { left: 191px; top: 687px; width: 820px; height: 121px; border-bottom: none; box-shadow: none; }
  .info-icon { position: absolute; }
  .info-block { position: absolute; font-size: 11px; line-height: 15px; }
  .info-block h3 { font-weight: 400; font-size: 11.5px; color: var(--blue); margin-bottom: 3px; }
  .site-footer .btn-blue { left: 649px; top: 28px; width: 144px; height: 32px; font-size: 18px; line-height: 34px; }
  .footer-rule { position: absolute; left: 20px; right: 20px; top: 82px; border-top: 1px dotted #999; }
  .copyright { position: absolute; left: 0; right: 0; top: 94px; text-align: center; font-size: 10.5px; color: var(--blue); }
</style>
</head>
<body>
  <header>
    <div class="brand">
      <span class="brand-mark"></span>
      <span class="brand-name">Зорника Мед</span>
    </div>
    <a class="call-box">
      <div class="call-label">Call now</div>
      <div class="call-number">0700 412 58</div>
      <svg width="22" height="22" viewBox="0 0 24 24" fill="#fff"><path d="M6.6 10.8a15.1 15.1 0 0 0 6.6 6.6l2.2-2.2a1 1 0 0 1 1-.25 11.4 11.4 0 0 0 3.6.57 1 1 0 0 1 1 1V20a1 1 0 0 1-1 1A17 17 0 0 1 3 4a1 1 0 0 1 1-1h3.5a1 1 0 0 1 1 1c0 1.250.2 2.450.57 3.570a1 1 0 0 1-.25 1z"/></svg>
    </a>
    <nav class="main-nav">
      <a class="is-active">Start</a>
      <a>Types of Headaches</a>
      <a>For us</a>
      <a>Contacts</a>
      <a>Blog</a>
    </nav>
    <div class="nav-rule"></div>
  </header>

  <section class="panel hero">
    <h1 class="hero-title">Hello!</h1>
    <div class="hero-text">
      <p>If you or your carer often suffer from headaches, here you can learn more about the<br>different types of headache (migraine, tension, cluster, hangover and many others),<br>our approach and to sign up for examination by us.</p>
      <p>We created the Zornika Med in 2014 to introduce modern methods in the<br>treatment of headaches. Our team of neurologists, neurosurgeons, physiotherapists<br>and psychiatrists is devoted to the study and treatment of this condition.</p>
    </div>
    <a class="hero-cta">
      <svg width="44" height="28" viewBox="0 0 44 28"><path d="M0 8h26V0l18 14-18 14v-8H0z" fill="var(--green)"/></svg>
      Check what type of headache you have
    </a>
    <div class="hero-figure" role="img" aria-label="Line drawing of a head from front and back with key headache pressure points marked"></div>
    <span class="slider-arrow slider-prev">‹</span>
    <span class="slider-arrow slider-next">›</span>
    <div class="slider-dots"><span class="is-active"></span><span></span><span></span></div>
  </section>

  <section class="panel blog">
    <h2 class="panel-head">From the blog</h2>
    <div class="post-thumb"></div>
    <article class="post-body">
      <h3 class="post-title">Work began on the site!</h3>
      <p class="post-date">Dec 16 2013 12:37 PM</p>
      <p class="post-excerpt">We hope the site to be practical and useful to people.</p>
      <a class="post-more">Read More</a>
    </article>
  </section>

  <section class="panel newsletter">
    <h2 class="panel-head">Newsletter</h2>
    <p class="newsletter-label">Subscribe to news Email</p>
    <input class="newsletter-input" type="text" value="Enter your email here">
    <a class="btn-blue">Read more</a>
  </section>

  <footer class="panel site-footer">
    <svg class="info-icon" style="left:18px;top:16px" width="46" height="48" viewBox="0 0 46 48">
      <rect width="46" height="48" rx="4" fill="var(--green-dark)"/>
      <circle cx="23" cy="24" r="15" fill="#fff"/>
      <circle cx="23" cy="24" r="12" fill="none" stroke="var(--green)" stroke-width="2"/>
      <path d="M23 15v9l6 4" stroke="var(--green-dark)" stroke-width="2.5" fill="none" stroke-linecap="round"/>
    </svg>
    <div class="info-block" style="left:73px;top:16px">
      <h3>HOURS</h3>
      <p>Monday &nbsp;- &nbsp;Friday</p>
      <p>8 : 00 to 18 : 00</p>
    </div>
    <svg class="info-icon" style="left:336px;top:14px" width="28" height="48" viewBox="0 0 28 48">
      <path d="M14 48C14 48 0 26 0 14a14 14 0 0 1 28 0c0 12-14 34-14 34z" fill="var(--green)"/>
      <circle cx="14" cy="14" r="5" fill="#fff"/>
    </svg>
    <div class="info-block" style="left:375px;top:16px">
      <h3>WHERE ARE WE ?</h3>
      <p>Sofia</p>
      <p>Blvd "Lozenska Reka"</p>
      <p>12</p>
    </div>
    <a class="btn-blue">Save your time now</a>
    <div class="footer-rule"></div>
    <p class="copyright">© 2013-2014 "Zornika Med" Ltd. All rights reserved. Powered by Larchwood</p>
  </footer>
</body>
</html>
```